Rivolex.com Trucking Company Website

Need a website designed (no content) for a trucking company, specializing in trucking of ocean containers (intermodal Trucking). Heavy emphasis on technology, using latest technology, providing unabated visibility and realtime information.
clean minimalist industrial website
example:
https://www.bramtiq.com/

Target Market(s)

Professional Business Consumer corporate and small business

Industry/Entity Type

Trucking Company

Number of Pages Required

5+ page

Requirements
Must have
• Industrial Design, simple informative, for a busy professional to view and get the necessary information with out the distractions.
• Blog Page
• Client Log-In on the front page
• Technology page - showing our intensive investments in technology
Nice to have
• If ANY images included, MUST be USA related. Example if include an image of a truck, ensure its a USA model. Do the research.
• included our business card for sample of Logo
• Doesnt not have to be the same color schemes.
Should not have
• moving images

```html
<!DOCTYPE html>
<html lang="en">
<head>
<meta charset="utf-8">
<title>Rivolex Consulting</title>
<link href="https://fonts.googleapis.com/css2?family=Open+Sans:wght@300;400;600;700&display=swap" rel="stylesheet">
<style>
:root{
  --ink:#111418;
  --nav:#15181d;
  --text:#333;
  --muted:#666;
  --footer:#f1f1f1;
  --rule:#d2d2d2;
  --partner:#9a9a9a;
  --white:#fff;
}
*{margin:0;padding:0;box-sizing:border-box}
html,body{width:1200px;height:1120px;overflow:hidden;background:var(--white);font-family:'Open Sans',sans-serif;color:var(--text)}
.page{position:absolute;left:313px;top:0;width:574px;height:1120px}
.abs{position:absolute}
.topbar{left:0;top:0;width:574px;height:39px;background:var(--nav)}
.brand{left:20px;top:10px;color:var(--white);line-height:1}
.brand-name{font-size:15px;font-weight:700;letter-spacing:1px}
.brand-sub{font-size:5px;letter-spacing:2.6px;margin-top:1px}
.menu{right:22px;top:19px;display:flex;align-items:center;font-size:7.5px;color:var(--white)}
.menu span.sep{margin:0 9px}
.menu .login{border:1px solid var(--white);padding:2px 9px;font-size:5.5px;margin-left:12px}
.hero{left:0;top:39px;width:574px;height:288px;background:linear-gradient(180deg,#9aa9c9 0%,#b8b9c8 40%,#8d7f7a 62%,#4a4b4f 80%,#2f3136 100%)}
.hero-tag{left:65px;top:154px;background:var(--ink);color:var(--white);font-size:16.5px;font-weight:300;padding:0 8px;height:27px;line-height:27px}
.hero-title{left:65px;top:183px;background:var(--ink);color:var(--white);font-size:38px;font-weight:700;padding:0 8px;height:49px;line-height:49px;letter-spacing:.5px}
.arrow{top:155px}
.section-kicker{left:0;width:574px;text-align:center;font-size:10px;font-weight:400;color:var(--text);letter-spacing:.3px}
.section-title{left:0;width:574px;text-align:center;font-size:23px;font-weight:300;color:var(--ink);letter-spacing:.5px}
.copy{left:45px;width:484px;text-align:center;font-size:6.2px;line-height:15.5px;color:var(--muted)}
.btn{border:1px solid var(--text);font-size:6px;color:var(--ink);text-align:center;line-height:16px;height:18px}
.band{left:0;top:559px;width:574px;height:155px;background:linear-gradient(90deg,#5b3a2c 0%,#6c5a45 30%,#e9ecec 45%,#dfe2e2 60%,#5d4b3a 75%,#4e3b2d 100%)}
.partners{left:25px;top:936px;width:524px;height:32px;display:flex;justify-content:space-between;align-items:center}
.partner{font-size:9px;font-weight:600;color:var(--partner);letter-spacing:.5px}
.footer{left:0;top:1000px;width:574px;height:120px;background:var(--footer)}
.social{left:240px;top:15px;display:flex;gap:8px}
.social i{display:block;width:12px;height:12px;border-radius:2px}
.rule{left:135px;width:304px;height:1px;background:var(--rule)}
.phone{left:0;width:574px;top:48px;text-align:center;font-size:19px;font-weight:600;color:#444}
.mail{left:0;width:574px;top:73px;text-align:center;font-size:11px;color:#444}
.legal{left:0;width:574px;top:104px;text-align:center;font-size:6.3px;letter-spacing:1px;color:var(--muted)}
.legal span{margin:0 12px}
</style>
</head>
<body>
<div class="page">
  <header class="abs topbar">
    <div class="abs brand"><div class="brand-name">RIVOLEX</div><div class="brand-sub">CONSULTING</div></div>
    <nav class="abs menu">
      <span>Home</span><span class="sep">|</span><span>About Us</span><span class="sep">|</span><span>Services</span><span class="sep">|</span><span>Technology</span><span class="sep">|</span><span>Blog</span><span class="login">LOGIN</span>
    </nav>
  </header>

  <section class="abs hero" role="img" aria-label="Silver semi truck driving on a coastal highway at dusk">
    <div class="abs hero-tag">YOUR HEADING</div>
    <div class="abs hero-title">GOES HERE</div>
    <svg class="abs arrow" style="left:0" width="17" height="32" viewBox="0 0 17 32"><path d="M0 0 L17 16 L0 32Z" fill="var(--ink)"/><path d="M7 13 L5 16 L7 19" stroke="#fff" stroke-width="1" fill="none"/></svg>
    <svg class="abs arrow" style="right:0" width="17" height="32" viewBox="0 0 17 32"><path d="M17 0 L0 16 L17 32Z" fill="var(--ink)"/><path d="M10 13 L12 16 L10 19" stroke="#fff" stroke-width="1" fill="none"/></svg>
  </section>

  <div class="abs section-kicker" style="top:370px">WELCOME TO</div>
  <h1 class="abs section-title" style="top:382px">RIVOLEX CONSULTING</h1>
  <p class="abs copy" style="top:430px">Lorem Ipsum is simply dummy text of the printing and typesetting industry. Lorem Ipsum has been the industry's standard dummy text ever since the 1500s, when an unknown printer took a galley of type and scrambled it to make a type specimen book. It has survived not only five centuries, but also the leap into electronic typesetting, remaining essentially unchanged. It was popularised in the 1960s with the release of Typorell sheets containing Lorem Ipsum passages, and more recently with desktop publishing software like Pagevant Studio including versions of Lorem Ipsum.</p>
  <div class="abs btn" style="left:244px;top:505px;width:85px">LOGIN</div>

  <div class="abs band" role="img" aria-label="White American semi truck with trailer on a rural road through autumn woods"></div>

  <div class="abs section-kicker" style="top:752px">RIVOLEX CONSULTING</div>
  <h2 class="abs section-title" style="top:764px">ABOUT US</h2>
  <p class="abs copy" style="top:812px">Lorem Ipsum is simply dummy text of the printing and typesetting industry. Lorem Ipsum has been the industry's standard dummy text ever since the 1500s, when an unknown printer took a galley of type and scrambled it to make a type specimen book. It has survived not only five centuries, but also the leap into electronic typesetting, remaining essentially unchanged. It was popularised in the 1960s</p>
  <div class="abs btn" style="left:243px;top:866px;width:85px">LEARN MORE</div>

  <div class="abs partners">
    <span class="partner">KORVANE</span><span class="partner">TAMROK</span><span class="partner">VELMORA</span><span class="partner">OSKARU</span><span class="partner">BRENHAL</span><span class="partner">QUIROS</span><span class="partner">ZELTAN</span><span class="partner">AMARELL</span>
  </div>

  <footer class="abs footer">
    <div class="abs social">
      <i style="background:#f4b940"></i><i style="background:#4fb1e0"></i><i style="background:#e06b9e"></i><i style="background:#6fd0dd"></i><i style="background:#4a69b8"></i>
    </div>
    <div class="abs rule" style="top:41px"></div>
    <div class="abs phone">0123-456-7890</div>
    <div class="abs mail">info@domain.com</div>
    <div class="abs rule" style="top:95px;left:0;width:574px"></div>
    <div class="abs legal">COPYRIGHT © 2017<span>|</span>RIVOLEX CONSULTING INC<span>|</span>ALL RIGHTS RESERVED.</div>
  </footer>
</div>
</body>
</html>
```